Marlow Crest Group (Real Estate and Investment)

A high end, clean design.
We are a real estate company with sales, asset management and investment divisions. We want to use a black and white scheme which is really high end feel. The back of the card can just be the logo (black background with the white writing) as we will probably emboss this when we print)

Target Market(s)

High level investors, high end houses for sale

Industry/Entity Type

Business

Contact Information for Business Card

Name, position, phone number and email address
Glen Varley, Managing Director, 0437259064 and glen@marlowcrest-example.com.au

Requirements
Must have
• Back of the card to be the black background with the white writing (as per the attached images). Would like the capacity to emboss the writing and logo

```html
<!DOCTYPE html>
<html lang="en">
<head>
<meta charset="utf-8">
<title>Marlow Crest Group – Business Card</title>
<link href="https://fonts.googleapis.com/css2?family=Open+Sans:wght@300;400;600&display=swap" rel="stylesheet">
<style>
  :root {
    --stage: #f1f1f1;
    --card-white: #ffffff;
    --card-black: #0b0b0c;
    --ink-dark: #141414;
    --ink-light: #ffffff;
    --ink-muted: #d9d9d9;
    --shadow: rgba(0, 0, 0, 0.12);
  }
  * { box-sizing: border-box; margin: 0; padding: 0; }
  html, body {
    width: 1200px;
    height: 780px;
    overflow: hidden;
  }
  body {
    background: var(--stage);
    font-family: "Open Sans", Arial, sans-serif;
    display: flex;
    flex-direction: column;
    align-items: center;
    justify-content: center;
    gap: 22px;
  }
  .card {
    width: 420px;
    height: 264px;
    border-radius: 18px;
    box-shadow: 0 6px 18px var(--shadow);
    position: relative;
  }
  .card--front {
    background: var(--card-white);
    display: flex;
    flex-direction: column;
    align-items: center;
    justify-content: center;
    gap: 20px;
  }
  .brand-mark {
    width: 64px;
    height: 64px;
  }
  .brand-name {
    font-weight: 300;
    font-size: 21px;
    letter-spacing: 0.5px;
    color: var(--ink-dark);
    text-transform: uppercase;
  }
  .card--back {
    background: var(--card-black);
    color: var(--ink-light);
  }
  .contact {
    position: absolute;
    left: 42px;
    top: 148px;
  }
  .contact__name {
    font-weight: 600;
    font-size: 16px;
    line-height: 1.15;
  }
  .contact__role {
    font-size: 9.5px;
    color: var(--ink-muted);
    margin-top: 2px;
  }
  .contact__phone {
    font-size: 11.5px;
    margin-top: 3px;
  }
  .contact__email {
    position: absolute;
    right: 24px;
    bottom: 52px;
    font-size: 11.5px;
  }
</style>
</head>
<body>
  <section class="card card--front" aria-label="Card front">
    <svg class="brand-mark" viewBox="0 0 64 64" aria-hidden="true">
      <circle cx="32" cy="32" r="30" fill="none" stroke="#141414" stroke-width="1.4"/>
    </svg>
    <p class="brand-name">Marlow Crest Group</p>
  </section>

  <section class="card card--back" aria-label="Card back">
    <div class="contact">
      <p class="contact__name">Glen Varley</p>
      <p class="contact__role">Managing Director</p>
      <p class="contact__phone">043 725 9064</p>
    </div>
    <p class="contact__email">glen@marlowcrest-example.com.au</p>
  </section>
</body>
</html>
```